Business card and Logo for a private personal training studio

We need a business card and logo for a private personal training studio.

The studios name is "Steady Your Path"
Main coloring to be a bright light blue. Looking for a crisp modern look

The front of the card is to have the

Studios name.
The Logo
Private Personal Training Studio
Mel Carver
0451 239 716

The back of the card is to have a lot of words relating to the services we offer. Please place the words vertically and horizontally using different fonts, different text sizes, different boldness and different colors to create a word picture.

Main words that need highlighting are

QVL, PILATES, BOXING, SPIN, STRENGTH, WEIGHT LOSS, BALANCE

Other words to add to the mix with less emphasis

Fitness, Conditioning, Lifestyle, Wellness, Health, Energy, Cardio, Goals, Muscle Tone, Vitality, Confidence, Attitude, Determination, Motivation, Dedication, Fun

Target Market(s)

Woman aged 30 to 60

Industry/Entity Type

Personal Trainer

Contact Information for Business Card

Steady Your Path
Mel Carver
0451 239 716

Colors
0493ce
33a6d7
85cae6

```html
<!DOCTYPE html>
<html lang="en">
<head>
<meta charset="utf-8">
<title>Steady Your Path – Business Card</title>
<link rel="stylesheet" href="https://fonts.googleapis.com/css2?family=Arimo:wght@400;700&family=Source+Sans+3:wght@400;600&display=swap">
<style>
  :root {
    --stage: #e9e6e1;
    --card-white: #ffffff;
    --card-black: #0b0b0c;
    --blue-deep: #0493ce;
    --blue-mid: #33a6d7;
    --blue-light: #85cae6;
    --text-white: #ffffff;
  }
  * { margin: 0; padding: 0; box-sizing: border-box; }
  html, body { width: 1200px; height: 892px; overflow: hidden; }
  body {
    background: var(--stage);
    display: flex;
    flex-direction: column;
    align-items: center;
    justify-content: center;
    gap: 40px;
  }
  .card {
    position: relative;
    width: 640px;
    height: 366px;
    border-radius: 4px;
    overflow: hidden;
    box-shadow: 0 6px 18px rgba(0,0,0,0.18);
  }

  /* Front */
  .card-front { background: var(--card-white); }
  .front-wave { position: absolute; inset: 0; width: 100%; height: 100%; }
  .logo-mark {
    position: absolute;
    left: 206px; top: 26px;
    width: 54px; height: 54px;
    border-radius: 50%;
    background: var(--blue-deep);
  }
  .studio-name {
    position: absolute;
    left: 262px; top: 88px;
    font-family: "Arimo", Arial, sans-serif;
    font-weight: 700;
    font-size: 40px;
    line-height: 1.1;
    color: var(--blue-deep);
    white-space: nowrap;
  }
  .studio-tagline {
    position: absolute;
    left: 266px; top: 140px;
    font-family: "Arimo", Arial, sans-serif;
    font-weight: 400;
    font-size: 17px;
    line-height: 1.1;
    color: var(--blue-mid);
    white-space: nowrap;
  }
  .trainer-name {
    position: absolute;
    right: 220px; top: 256px;
    font-family: "Arimo", Arial, sans-serif;
    font-size: 38px;
    line-height: 1.1;
    color: var(--text-white);
    white-space: nowrap;
  }
  .trainer-phone {
    position: absolute;
    right: 252px; top: 314px;
    display: flex;
    align-items: center;
    gap: 12px;
    font-family: "Arimo", Arial, sans-serif;
    font-size: 22px;
    line-height: 1.1;
    color: var(--text-white);
    white-space: nowrap;
  }
  .phone-badge {
    width: 15px; height: 15px;
    background: var(--blue-deep);
  }

  /* Back */
  .card-back {
    background: var(--card-black);
    display: flex;
    flex-direction: column;
    justify-content: center;
    align-items: center;
    gap: 22px;
    font-family: "Source Sans 3", "Myriad Pro", sans-serif;
    color: var(--blue-light);
  }
  .word-line {
    display: flex;
    align-items: baseline;
    gap: 12px;
    white-space: nowrap;
    font-size: 21px;
  }
  .word-key {
    font-size: 28px;
    font-weight: 400;
    text-decoration: underline;
    text-underline-offset: 5px;
    text-decoration-thickness: 1px;
    color: var(--blue-light);
  }
</style>
</head>
<body>

  <section class="card card-front">
    <svg class="front-wave" viewBox="0 0 640 366" preserveAspectRatio="none" aria-hidden="true">
      <path d="M0,0 L140,0 C190,150 280,205 410,240 C530,272 600,298 628,366 L0,366 Z" fill="var(--blue-mid)"/>
      <path d="M0,0 L120,0 C170,160 260,222 400,256 C520,286 580,306 604,366 L0,366 Z" fill="var(--card-black)"/>
    </svg>
    <div class="logo-mark"></div>
    <h1 class="studio-name">Steady Your Path</h1>
    <p class="studio-tagline">Private Personal Training Studio</p>
    <p class="trainer-name">Mel Carver</p>
    <p class="trainer-phone">0451 239 716 <span class="phone-badge"></span></p>
  </section>

  <section class="card card-back">
    <p class="word-line"><span class="word-key">QVL</span> Fitness <span class="word-key">PILATES</span> Conditioning</p>
    <p class="word-line">Wellness <span class="word-key">SPIN</span> Health <span class="word-key">STRENGTH</span> Energy</p>
    <p class="word-line">Goals, Muscle Tone, Vitality, Confidence, Attitude</p>
    <p class="word-line">Determination, <span class="word-key">WEIGHT LOSS</span> Motivation, Dedication</p>
  </section>

</body>
</html>
```